Business card design needed

I have started a new business called Marlow Auto Electrical, although the words Marlow Auto Electrical will be used on signage and documents I actually want to market the business as MAE. The services I offer are Mobile Auto Electrical, Automotive Air Conditioning and Test And Tag. My business will be targetting the Mining Industry, Civil, Rail, Agricultural and Workshop Testing And Tagging. My auto electrical service ranges from fault finding to new vehicle and mine compliance fit outs. I have a very strong focus on quality workmanship. I will upload the logo I have designed and want to use I am happy for the logo colour to change but the design itself must stay the same. I want the design to have a modern, eye catching, energetic feel. As I am a passionate motorsport fan I am happy for this to also influence the design. I am happy for the front of the card to have only the emblem and logo design and the back to have all the info.

Industry/Entity Type

Electrical

Contact Information for Business Card

MAE Marlow Auto Electrical, Dale Penrick, Auto Electrician, Mobile No 0417263859

Requirements
Must have
• On the business card it is mandatory that the following license numbers are shown:

MVRL38462
VDA L071348
ABN 61 839 204 518

```html
<!DOCTYPE html>
<html lang="en">
<head>
<meta charset="utf-8">
<title>Marlow Auto Electrical – Business Card</title>
<link href="https://fonts.googleapis.com/css2?family=Archivo+Black&family=Kalam:wght@700&display=swap" rel="stylesheet">
<style>
  :root {
    --ink: #050505;
    --signal-yellow: #ffd400;
    --card-w: 1200px;
    --card-h: 741px;
    --band-top: 505px;
  }
  * { margin: 0; padding: 0; box-sizing: border-box; }
  html, body {
    width: var(--card-w);
    height: var(--card-h);
    overflow: hidden;
    background: var(--signal-yellow);
  }
  .card {
    position: relative;
    width: var(--card-w);
    height: var(--card-h);
    background: var(--signal-yellow);
    font-family: "Archivo Black", "Arial Black", sans-serif;
    color: var(--ink);
    overflow: hidden;
  }
  .brand-panel {
    position: absolute;
    inset: 0 0 auto 0;
    height: var(--band-top);
    background: var(--ink);
  }
  .panel-edge {
    position: absolute;
    left: 0;
    top: calc(var(--band-top) - 1px);
    width: var(--card-w);
    height: 10px;
    display: block;
  }
  .brand-mark {
    position: absolute;
    left: 0;
    right: 0;
    top: 150px;
    display: flex;
    justify-content: center;
    align-items: center;
    gap: 34px;
  }
  .brand-square {
    width: 110px;
    height: 110px;
    background: var(--signal-yellow);
  }
  .brand-initials {
    font-size: 120px;
    line-height: 1;
    color: var(--signal-yellow);
  }
  .brand-name {
    position: absolute;
    left: 0;
    right: 0;
    top: 378px;
    text-align: center;
    font-family: "Kalam", "Comic Sans MS", cursive;
    font-weight: 700;
    font-size: 78px;
    line-height: 1.1;
    letter-spacing: 2px;
    color: var(--signal-yellow);
    text-transform: uppercase;
  }
  .contact {
    position: absolute;
    left: 0;
    right: 0;
    text-align: center;
    text-transform: uppercase;
    line-height: 1;
  }
  .contact-name { top: 546px; font-size: 37px; letter-spacing: 1.5px; }
  .contact-mobile { top: 596px; font-size: 37px; letter-spacing: 1.5px; }
  .licences {
    position: absolute;
    left: 0;
    right: 0;
    top: 672px;
    text-align: center;
    font-size: 24px;
    letter-spacing: 6px;
    word-spacing: 6px;
    line-height: 1;
  }
</style>
</head>
<body>
  <main class="card">
    <section class="brand-panel">
      <div class="brand-mark">
        <span class="brand-square" aria-hidden="true"></span>
        <span class="brand-initials">MAE</span>
      </div>
      <div class="brand-name">Marlow Auto Electrical</div>
    </section>
    <svg class="panel-edge" viewBox="0 0 1200 10" aria-hidden="true">
      <defs>
        <pattern id="edge-teeth" width="36" height="10" patternUnits="userSpaceOnUse">
          <rect x="0" y="0" width="36" height="2" fill="#050505"/>
          <rect x="6" y="0" width="22" height="8" fill="#050505"/>
        </pattern>
      </defs>
      <rect width="1200" height="10" fill="url(#edge-teeth)"/>
    </svg>
    <p class="contact contact-name">Dale Penrick, Auto Electrician</p>
    <p class="contact contact-mobile">Mobile No 0417263859</p>
    <p class="licences">MVRL38462 • VDA L071348 • ABN 61 839 204 518</p>
  </main>
</body>
</html>
```